Modernes, ausgefallenes Honigglas-Etikett
Zielgruppe
Ich bin neuer Imker in der Region und möchte meinem Honig regional vermarkten.
Zielgruppe sind gesundheitsbewußte Kunden.
Aufgabenstellung
Zum Glas: Ich verwende zwei verschiedene Kormalit Sturzgläser mit 250g (210er) bzw. 500g (410er). Hierfür benötige ich zwei passende Etiketten. Der zugehörige Deckel ist schwarz.
Zum Etikett: Das Etikett sollte transparent und alternativ auch aus Papier sein (der Nachhaltigkeit Willen) Das Etikett sollte für alle Sorten einheitlich sein.
Meine Vorlieben, die aber nicht unbedingt beeinflussen sollten, wenn das Gesamtbild stimmig ist. Ich mag es 'aufgeräumt' und nicht zu überladen. Gradlinige Schrifttypen bzw. moderne Schrifttypen.
Sorten zum Beginn der Imkerei Blütenhonig, Waldhonig
Zum „Hauptmotiv“ Ich stelle mir einen Bären a la WaldKnopf/Moosgreifer/Zweigfreund vor. Nicht zu verspielt, nicht zu lieb
Beispiele, die ich finden konnte füge ich als Anlage bei. Das Symbol Biene finde ich zu „abgegriffen“ und sollte nicht im Fokus stehen. Deckel: Ein rundes Etikett ggf. verbunden mit dem Gewährverschluss, Angabe des zur Mindesthaltbarkeit, Mindestens haltbar bis (taggenau), Mehrwegglas.
Zum Gewährverschluss:
Der Gewährverschluss ist ggf. farbig bzw. Sortenspezifisch. Oder es wird nur die Sorte namentlich genannt ohne Farbcodierung. Je nachdem wie es zum Gesamt-Layout passt.
Pflichtangaben auf dem Glas:
Ursprungsland (Deutschland), Imkerhonig / Honig, Mengenangabe “℮“ 250g / 500g, Name und komplette Anschrift des Imkers (zusätzlich Email und Webadresse), Mindestens haltbar bis: (Tagesdatum), Mehrwegglas, Honig gut verschlossen, kühl (maximal 15°C), dunkel und trocken lagern.

```html
<!DOCTYPE html>
<html lang="de">
<head>
<meta charset="utf-8">
<title>Moosgreifer Waldhonig – Etikett</title>
<link href="https://fonts.googleapis.com/css2?family=Montserrat:wght@500;600&family=Kaushan+Script&display=swap" rel="stylesheet">
<style>
  :root {
    --backdrop: #1e140e;
    --label: #f4c763;
    --label-light: #f7cf72;
    --label-ink: #fff8ea;
    --variety-green: #235a47;
  }
  html, body {
    margin: 0;
    padding: 0;
    width: 1200px;
    height: 1181px;
    overflow: hidden;
    background: var(--backdrop);
  }
  .canvas {
    position: relative;
    width: 1200px;
    height: 1181px;
  }
  .label {
    position: absolute;
    left: 174px;
    top: 90px;
    width: 852px;
    height: 1000px;
    background: var(--label);
    font-family: "Montserrat", sans-serif;
    color: var(--label-ink);
    text-align: center;
  }
  .label__texture {
    position: absolute;
    inset: 0;
    background: radial-gradient(ellipse at 60% 45%, var(--label-light), var(--label) 70%);
  }
  .label__tag {
    position: absolute;
    top: 58px;
    left: 0;
    right: 0;
    font-weight: 600;
    font-size: 34px;
    letter-spacing: 2px;
  }
  .brand {
    position: absolute;
    top: 250px;
    left: 0;
    right: 0;
  }
  .brand__dot {
    display: block;
    margin: 0 auto 40px;
  }
  .brand__name {
    font-weight: 600;
    font-size: 80px;
    letter-spacing: 5px;
    line-height: 1;
  }
  .variety {
    position: absolute;
    top: 555px;
    left: 0;
    right: 0;
    font-family: "Kaushan Script", cursive;
    font-size: 104px;
    color: var(--variety-green);
    line-height: 1;
  }
  .net-weight {
    position: absolute;
    bottom: 42px;
    left: 0;
    right: 0;
    font-weight: 600;
    font-size: 30px;
  }
</style>
</head>
<body>
<main class="canvas">
  <section class="label">
    <div class="label__texture" role="img" aria-label="Dezentes Wabenmuster auf dem Etikett"></div>
    <div class="label__tag">– BIO –</div>
    <div class="brand">
      <svg class="brand__dot" width="150" height="150" viewBox="0 0 150 150" aria-hidden="true">
        <circle cx="75" cy="75" r="68" fill="none" stroke="var(--label-ink)" stroke-width="6"/>
      </svg>
      <div class="brand__name">MOOSGREIFER</div>
    </div>
    <div class="variety">Waldhonig</div>
    <div class="net-weight">490 g</div>
  </section>
</main>
</body>
</html>
```